Norvane Staffing - White Collar Engineering Consultancy

I'm chasing a website to provide high level information about what Norvane Staffing is and service's we provide - only chasing something simple. We are a new white collar secondment/contractor/professional services/consultancy specialising is providing the best consultants into contractor roles.

Our primary industries are energy, gas, pipelines, water processing, power, projects, geographic information systems, design, accounting.

Our people are mechanical,/electrical/civil/process/chemical engineers, project engineers, project managers, technical experts, GIS analysts, integrity engineers, pipeline engineers,

Currently I have this domain registered through Zentrio - https://www.norvanestaffing-example.com/

I'd like to keep this domain but completely overhaul the website to be sleek and follow the logo styling.

Example websites within my industry that I like:
- https://www.brelwickworks-example.com.au/
- https://quarn-example.com.au/
- https://www.hdmtech-example.com.au/

I'd like the winner to code and assist with making the website functional under my domain.

Would like to include:
- industries
- services
- why work with us
- terms and conditions as per attached
- location (Brisbane)
- contact us form, that submits an email to sam.burow@norvanestaffing-example.com
- WorkLinker link

Would definitely be looking to polish the winning result with the designer over the phone or via email.

I will also add some infrastructure photos for use; otherwise please use generic CSG related infrastructure.

Cheers,

Sam

Industry/Entity Type

Energy, resources, gas, mining, geographic information systems, accounting, construction.

Coding

Coded - Design and coding required

Number of Pages Required

4 page

Colors
0054AA
0677BA
7BADD7
CADEEF
E8F1F8

Requirements
Must have
• Refer to project description

```html
<!DOCTYPE html>
<html lang="en">
<head>
<meta charset="utf-8">
<title>Norvane Staffing - White Collar Engineering Consultancy</title>
<link rel="stylesheet" href="https://fonts.googleapis.com/css2?family=Poppins:ital,wght@0,400;0,500;0,600;0,700;1,700;1,800&display=swap">
<style>
:root{
  --primary:#0054AA;
  --mid:#0677BA;
  --soft:#7BADD7;
  --pale:#CADEEF;
  --mist:#E8F1F8;
  --navy:#0d2150;
  --gold:#d9a441;
  --ink:#1b1b1b;
  --footer:#242424;
  --white:#ffffff;
}
*{box-sizing:border-box;margin:0;padding:0}
html,body{width:1200px;height:4264px;overflow:hidden}
body{font-family:'Poppins',sans-serif;color:var(--ink);background:var(--white);position:relative}
.h-title{font-weight:800;font-style:italic;text-transform:uppercase;letter-spacing:1px}
.btn{display:inline-block;background:var(--primary);color:var(--white);font-weight:600;font-size:15px;text-transform:uppercase;border-radius:26px;padding:16px 30px;text-decoration:none}

/* header */
.site-header{position:absolute;top:0;left:0;width:1200px;height:92px;display:flex;align-items:center;padding:0 48px;background:var(--white);z-index:2}
.brand{display:flex;align-items:center;gap:12px;font-weight:700;font-size:30px;color:var(--navy)}
.brand-dot{width:36px;height:36px;border-radius:50%;background:var(--navy)}
.main-nav{margin-left:auto;display:flex;gap:34px;font-size:16px;font-weight:500}
.main-nav a{color:var(--ink);text-decoration:none}
.header-cta{margin-left:40px;padding:14px 26px;font-size:14px}
.social{margin-left:18px;display:flex;align-items:center;gap:6px;font-size:13px;font-weight:600;color:var(--primary)}
.social-ring{width:22px;height:22px;border:2px solid var(--primary);border-radius:50%}

/* hero */
.hero{position:absolute;top:92px;left:0;width:1200px;height:596px;border-bottom-right-radius:150px;overflow:hidden;
  background:
    linear-gradient(180deg,rgba(0,0,0,0) 55%,rgba(30,30,40,.65) 100%),
    linear-gradient(100deg,#1a2540 0%,#4d5668 35%,#9b8a74 60%,#e2b77c 85%,#f2d29a 100%)}
.hero-shade{position:absolute;inset:0;background:linear-gradient(90deg,rgba(10,20,45,.78) 0%,rgba(10,20,45,.35) 50%,rgba(10,20,45,0) 100%)}
.hero-copy{position:absolute;left:108px;top:160px;width:470px;color:var(--white)}
.hero-copy h1{font-size:44px;line-height:1.15;font-weight:800;font-style:italic;text-transform:uppercase}
.hero-copy p{font-size:16px;line-height:1.5;margin:22px 0 38px}

/* why */
.why{position:absolute;top:740px;left:0;width:1200px;text-align:center}
.why h2{font-size:32px;margin-bottom:22px}
.why .intro{width:960px;margin:0 auto;font-size:16px;line-height:1.55}
.why-list{display:flex;justify-content:center;gap:110px;margin-top:42px}
.why-item{width:150px;display:flex;flex-direction:column;align-items:center;font-size:20px;line-height:1.25}
.why-icon{width:130px;height:130px;border-radius:50%;border:2px solid var(--pale);background:var(--white);margin-bottom:14px;display:flex;align-items:center;justify-content:center;box-shadow:0 4px 14px rgba(0,84,170,.08)}

/* industries */
.industries{position:absolute;top:1168px;left:0;width:1200px;height:632px;border-top-left-radius:150px;overflow:hidden;
  background:linear-gradient(180deg,#2a4a78 0%,#51668f 38%,#c08562 62%,#3a3f5a 78%,#141c34 100%)}
.industry-panel{position:absolute;left:582px;top:72px;width:520px;height:488px;background:rgba(13,33,80,.88);color:var(--white);padding:34px 36px}
.industry-panel h2{font-size:32px;margin-bottom:14px}
.industry-panel p{font-size:16px;line-height:1.5;margin-bottom:16px}
.industry-panel ul{list-style:none;font-size:17px;font-weight:600;line-height:1.62}
.industry-panel li{display:flex;align-items:center;gap:8px}
.industry-panel li::before{content:"";width:14px;height:14px;border-radius:50%;background:var(--white);box-shadow:inset 0 0 0 4px var(--soft)}

/* services */
.services{position:absolute;top:1800px;left:0;width:1200px;height:1060px;background:var(--mist);border-bottom-right-radius:150px;text-align:center}
.services h2{font-size:32px;margin-top:62px;margin-bottom:42px}
.service-grid{display:grid;grid-template-columns:repeat(4,232px);gap:32px 24px;justify-content:center;text-align:left}
.service-card{height:338px;border-bottom:3px solid var(--navy)}
.service-photo{height:160px}
.ph-mech{background:linear-gradient(135deg,#cfc6b8,#8a7a66 55%,#3d3a3a)}
.ph-elec{background:linear-gradient(160deg,#f1c232,#d08a2a 40%,#2e4f86 75%,#1d2c4d)}
.ph-civil{background:linear-gradient(160deg,#c9d4e0,#7d8796 50%,#3b3f48)}
.ph-proc{background:linear-gradient(150deg,#4e5566,#2a2f3b 60%,#d7a76a)}
.ph-chem{background:linear-gradient(150deg,#eef4f8,#a9cde3 50%,#4a7fa8)}
.ph-proj{background:linear-gradient(150deg,#d7c2a4,#8c6a4c 55%,#3a2e28)}
.ph-pm{background:linear-gradient(150deg,#f2ece4,#cbb79d 50%,#6e5846)}
.ph-tech{background:linear-gradient(150deg,#c7d8ec,#3f6eb3 50%,#1a2f5c)}
.service-card h3{font-size:19px;font-weight:600;color:var(--primary);margin:14px 0 6px}
.service-card p{font-size:12.5px;line-height:1.5}
.service-arrow{display:block;margin-top:12px}
.view-more{margin-top:56px}

/* location */
.location{position:absolute;top:2880px;left:0;width:1200px;height:480px}
.location-copy{position:absolute;left:108px;top:100px;width:380px}
.location-copy h2{font-size:32px;margin-bottom:16px}
.location-copy p{font-size:15px;line-height:1.5}
.city{display:flex;align-items:center;gap:6px;font-weight:700;font-size:17px;color:var(--primary);margin:16px 0 22px}
.map{position:absolute;left:700px;top:20px;width:460px;height:420px;border-radius:40px 60px 90px 120px;background:linear-gradient(150deg,#e4e6ea 0%,#c9ccd2 60%,#b8bcc4 100%)}
.map-pin{position:absolute;right:42px;top:150px}

/* contact */
.contact{position:absolute;top:3392px;left:0;width:1200px;height:548px;border-top-left-radius:150px;overflow:hidden;background:linear-gradient(180deg,#1c2e63 0%,#2b3c78 55%,#141c3c 100%);text-align:center}
.contact h2{font-size:32px;color:var(--white);margin-top:70px;margin-bottom:28px}
.contact-form{position:absolute;left:120px;top:150px;width:952px;height:152px}
.field{position:absolute;left:0;width:472px;height:46px;background:var(--white);font-size:15px;padding:13px 14px;text-align:left;color:#555}
.field.message{left:488px;top:0;width:464px;height:190px}
.submit{position:absolute;left:410px;top:232px;padding:14px 36px;font-size:14px}

/* footer */
.site-footer{position:absolute;top:3940px;left:0;width:1200px;height:324px;background:var(--footer);color:var(--white);text-align:center}
.footer-brand{display:flex;justify-content:center;align-items:center;gap:16px;margin-top:42px;font-size:40px;font-weight:700}
.footer-brand .brand-dot{width:70px;height:70px;background:var(--white)}
.footer-nav{display:flex;justify-content:center;gap:22px;font-size:15px;margin-top:46px}
.footer-nav span{opacity:.7}
.footer-contact{display:flex;justify-content:center;gap:22px;font-size:15px;margin-top:18px;align-items:center}
.copyright{font-size:13px;margin-top:22px;opacity:.9}
</style>
</head>
<body>

<header class="site-header">
  <div class="brand"><span class="brand-dot"></span>Norvane Staffing</div>
  <nav class="main-nav">
    <a href="#">Industries</a><a href="#">Services</a><a href="#">Why Work With Us</a><a href="#">Location</a>
  </nav>
  <a class="btn header-cta" href="#">Contact Us</a>
  <span class="social"><span class="social-ring"></span>WorkLinker</span>
</header>

<section class="hero" role="img" aria-label="Two engineers in hard hats looking at an industrial gas processing plant at sunset">
  <div class="hero-shade"></div>
  <div class="hero-copy">
    <h1>Welcome to Norvane Staffing</h1>
    <p>Lorem ipsum dolor sit amet, consectetur adipiscing elit, sed do eiusmod tempor incididunt ut labore et dolore magna aliqua.</p>
    <a class="btn" href="#">Get Started</a>
  </div>
</section>

<section class="why">
  <h2 class="h-title">Why Work With Us</h2>
  <p class="intro">Lorem ipsum dolor sit amet, consectetur adipiscing elit, sed do eiusmod tempor incididunt ut labore et dolore magna aliqua. Quis ipsum suspendisse ultrices gravida. Risus commodo viverra maecenas accumsan lacus vel facilisis.</p>
  <div class="why-list">
    <div class="why-item"><span class="why-icon"><svg width="70" height="70" viewBox="0 0 70 70" fill="none" stroke="#0054AA" stroke-width="2.4"><rect x="25" y="6" width="20" height="14" rx="2"/><rect x="4" y="48" width="18" height="14" rx="2"/><rect x="26" y="48" width="18" height="14" rx="2"/><rect x="48" y="48" width="18" height="14" rx="2"/><path d="M35 20v14M13 48V34h44v14M35 34v14"/></svg></span>Secondment</div>
    <div class="why-item"><span class="why-icon"><svg width="70" height="70" viewBox="0 0 70 70" fill="none" stroke="#0054AA" stroke-width="2.4"><rect x="8" y="22" width="54" height="36" rx="4"/><path d="M26 22v-6a3 3 0 0 1 3-3h12a3 3 0 0 1 3 3v6M8 38h54"/><rect x="30" y="34" width="10" height="8" rx="1" fill="#7BADD7"/></svg></span>Contractor</div>
    <div class="why-item"><span class="why-icon"><svg width="70" height="70" viewBox="0 0 70 70" fill="none" stroke="#0677BA" stroke-width="2.4"><circle cx="35" cy="35" r="10"/><path d="M35 8v9M35 53v9M8 35h9M53 35h9M16 16l6 6M48 48l6 6M16 54l6-6M48 22l6-6"/><circle cx="35" cy="35" r="18"/></svg></span>professional Services</div>
    <div class="why-item"><span class="why-icon"><svg width="70" height="70" viewBox="0 0 70 70" fill="none" stroke="#d9a441" stroke-width="2.4"><path d="M8 12h36a4 4 0 0 1 4 4v18a4 4 0 0 1-4 4H22l-10 8v-8H8a4 4 0 0 1-4-4V16a4 4 0 0 1 4-4z"/><path d="M52 26h10a4 4 0 0 1 4 4v16a4 4 0 0 1-4 4h-4v8l-10-8H34a4 4 0 0 1-4-4v-4" stroke="#0054AA"/><path d="M14 22h24M14 29h16"/></svg></span>Consultancy Specialising</div>
  </div>
</section>

<section class="industries" role="img" aria-label="City skyline with towers and cranes at dusk">
  <div class="industry-panel">
    <h2 class="h-title">Industries</h2>
    <p>Lorem ipsum dolor sit amet, consectetur adipiscing elit, sed do eiusmod tempor incididunt ut labore et dolore magna aliqua.</p>
    <ul>
      <li>Oil</li><li>Gas</li><li>Pipelines</li><li>Water Processingenergy</li><li>Energy</li><li>Power</li><li>Projects</li><li>Geographic</li><li>Information Systems</li>
    </ul>
  </div>
</section>

<section class="services">
  <h2 class="h-title">Our Services</h2>
  <div class="service-grid">
    <article class="service-card"><div class="service-photo ph-mech" role="img" aria-label="Mechanical engineer at work in a workshop"></div><h3>Mechanical</h3><p>Lorem ipsum dolor sit amet, elit, sed do eiusmod tempor incididunt ut labore et dolore magna aliqua. Quis ipsum suspendisse ultrices gravida.</p><svg class="service-arrow" width="18" height="18" viewBox="0 0 18 18"><circle cx="9" cy="9" r="8" fill="none" stroke="#0d2150" stroke-width="1.6"/><path d="M5 9h7M9 6l3 3-3 3" fill="none" stroke="#0d2150" stroke-width="1.6"/></svg></article>
    <article class="service-card"><div class="service-photo ph-elec" role="img" aria-label="Electrical engineer with yellow hard hat"></div><h3>Electrical</h3><p>Lorem ipsum dolor sit amet, elit, sed do eiusmod tempor incididunt ut labore et dolore magna aliqua. Quis ipsum suspendisse ultrices gravida.</p><svg class="service-arrow" width="18" height="18" viewBox="0 0 18 18"><circle cx="9" cy="9" r="8" fill="none" stroke="#0d2150" stroke-width="1.6"/><path d="M5 9h7M9 6l3 3-3 3" fill="none" stroke="#0d2150" stroke-width="1.6"/></svg></article>
    <article class="service-card"><div class="service-photo ph-civil" role="img" aria-label="Civil construction site with steel frame"></div><h3>Civil</h3><p>Lorem ipsum dolor sit amet, elit, sed do eiusmod tempor incididunt ut labore et dolore magna aliqua. Quis ipsum suspendisse ultrices gravida.</p><svg class="service-arrow" width="18" height="18" viewBox="0 0 18 18"><circle cx="9" cy="9" r="8" fill="none" stroke="#0d2150" stroke-width="1.6"/><path d="M5 9h7M9 6l3 3-3 3" fill="none" stroke="#0d2150" stroke-width="1.6"/></svg></article>
    <article class="service-card"><div class="service-photo ph-proc" role="img" aria-label="Process engineers inside an industrial plant"></div><h3>Process</h3><p>Lorem ipsum dolor sit amet, elit, sed do eiusmod tempor incididunt ut labore et dolore magna aliqua. Quis ipsum suspendisse ultrices gravida.</p><svg class="service-arrow" width="18" height="18" viewBox="0 0 18 18"><circle cx="9" cy="9" r="8" fill="none" stroke="#0d2150" stroke-width="1.6"/><path d="M5 9h7M9 6l3 3-3 3" fill="none" stroke="#0d2150" stroke-width="1.6"/></svg></article>
    <article class="service-card"><div class="service-photo ph-chem" role="img" aria-label="Chemical engineers in a bright laboratory"></div><h3>chemical Engineers</h3><p>Lorem ipsum dolor sit amet, elit, sed do eiusmod tempor incididunt ut labore et dolore magna aliqua. Quis ipsum suspendisse ultrices gravida.</p><svg class="service-arrow" width="18" height="18" viewBox="0 0 18 18"><circle cx="9" cy="9" r="8" fill="none" stroke="#0d2150" stroke-width="1.6"/><path d="M5 9h7M9 6l3 3-3 3" fill="none" stroke="#0d2150" stroke-width="1.6"/></svg></article>
    <article class="service-card"><div class="service-photo ph-proj" role="img" aria-label="Project engineers reviewing plans at a table"></div><h3>Project Engineers</h3><p>Lorem ipsum dolor sit amet, elit, sed do eiusmod tempor incididunt ut labore et dolore magna aliqua. Quis ipsum suspendisse ultrices gravida.</p><svg class="service-arrow" width="18" height="18" viewBox="0 0 18 18"><circle cx="9" cy="9" r="8" fill="none" stroke="#0d2150" stroke-width="1.6"/><path d="M5 9h7M9 6l3 3-3 3" fill="none" stroke="#0d2150" stroke-width="1.6"/></svg></article>
    <article class="service-card"><div class="service-photo ph-pm" role="img" aria-label="Project manager in a light office"></div><h3>project Managers</h3><p>Lorem ipsum dolor sit amet, elit, sed do eiusmod tempor incididunt ut labore et dolore magna aliqua. Quis ipsum suspendisse ultrices gravida.</p><svg class="service-arrow" width="18" height="18" viewBox="0 0 18 18"><circle cx="9" cy="9" r="8" fill="none" stroke="#0d2150" stroke-width="1.6"/><path d="M5 9h7M9 6l3 3-3 3" fill="none" stroke="#0d2150" stroke-width="1.6"/></svg></article>
    <article class="service-card"><div class="service-photo ph-tech" role="img" aria-label="Technical expert in blue overalls at a control panel"></div><h3>Technical Experts</h3><p>Lorem ipsum dolor sit amet, elit, sed do eiusmod tempor incididunt ut labore et dolore magna aliqua. Quis ipsum suspendisse ultrices gravida.</p><svg class="service-arrow" width="18" height="18" viewBox="0 0 18 18"><circle cx="9" cy="9" r="8" fill="none" stroke="#0d2150" stroke-width="1.6"/><path d="M5 9h7M9 6l3 3-3 3" fill="none" stroke="#0d2150" stroke-width="1.6"/></svg></article>
  </div>
  <a class="btn view-more" href="#">View More</a>
</section>

<section class="location">
  <div class="location-copy">
    <h2 class="h-title">Location</h2>
    <p>Lorem ipsum dolor sit amet, consectetur adipiscing elit, sed do eiusmod tempor incididunt ut labore et dolore magna aliqua. Quis ipsum suspendisse ultrices gravida.</p>
    <div class="city"><svg width="16" height="20" viewBox="0 0 16 20"><path d="M8 0C3.6 0 0 3.4 0 7.8 0 13 8 20 8 20s8-7 8-12.2C16 3.4 12.4 0 8 0z" fill="#0054AA"/><circle cx="8" cy="7.6" r="3" fill="#fff"/></svg>Brisbane</div>
    <a class="btn" href="#">Get Directions</a>
  </div>
  <div class="map" role="img" aria-label="Map of Australia with states labelled and a pin on Brisbane">
    <svg class="map-pin" width="26" height="34" viewBox="0 0 16 20"><path d="M8 0C3.6 0 0 3.4 0 7.8 0 13 8 20 8 20s8-7 8-12.2C16 3.4 12.4 0 8 0z" fill="#0054AA"/><circle cx="8" cy="7.6" r="3" fill="#fff"/></svg>
  </div>
</section>

<section class="contact" role="img" aria-label="Brisbane river and city skyline at night with blue overlay">
  <h2 class="h-title">Contact Us</h2>
  <form class="contact-form">
    <div class="field" style="top:0">Name*</div>
    <div class="field" style="top:72px">Email*</div>
    <div class="field" style="top:144px">Phone</div>
    <div class="field message">Message</div>
    <span class="btn submit">Submit</span>
  </form>
</section>

<footer class="site-footer">
  <div class="footer-brand"><span class="brand-dot"></span>Norvane Staffing</div>
  <nav class="footer-nav">
    <span>Home</span><span>|</span><span>Industries</span><span>|</span><span>Services</span><span>|</span><span>Why Work With Us</span><span>|</span><span>Location</span><span>|</span><span>Contact Us</span>
  </nav>
  <div class="footer-contact">
    <span>&#9679; Brisbane</span><span>|</span><span>&#9993; sam.burow@norvanestaffing-example.com</span><span>|</span><span>&#9742; +61 400 000 000</span>
  </div>
  <p class="copyright">Copyright &copy; 2023 Norvane Staffing Pty Ltd | All Rights Reserved | Terms And Conditions</p>
</footer>

</body>
</html>
```